Brightwell Giving Inc

We need a full re-design of our non-profit organization website (www.brightwellgiving.org). Ideally, we are looking to make it more attractive, user-friendly, and interactive with our business model.

Please make sure to user colors that ago with our logo.

We need a homepage done and we also need a content page done where we will use for the other pages to fill with content.

Target Market(s)

Clothes/textiles donations.

Industry/Entity Type

Charity

Number of Pages Required

2 page

Colors

Designer to choose colors to be used in the design.

Requirements
Must have
• It must match the styling of our logo and same colors as current website. (www.brightwellgiving.org)
Nice to have
• Sleek homepage that is easy to understand and get our main points across.

```html
<!DOCTYPE html>
<html lang="en">
<head>
<meta charset="utf-8">
<title>Brightwell Giving</title>
<link rel="stylesheet" href="https://fonts.googleapis.com/css2?family=Poppins:wght@400;600;700&family=Roboto:wght@400;500;700&display=swap">
<style>
:root{
  --green:#4b8b2b;
  --green-light:#6aac3a;
  --green-dark:#3a7020;
  --green-text:#4f8c2c;
  --topbar:#2a2420;
  --search:#3b3430;
  --grey-card:#e8e8e8;
  --text:#333333;
  --white:#ffffff;
}
*{box-sizing:border-box;margin:0;padding:0}
html,body{width:1200px;height:3309px;overflow:hidden}
body{position:relative;font-family:"Roboto",Arial,sans-serif;color:var(--text);background:var(--white)}
.abs{position:absolute}

/* top bar */
.topbar{left:0;top:0;width:1200px;height:55px;background:var(--topbar);color:var(--white);font-size:14px;font-weight:700}
.topbar .phone{top:19px}
.topbar .search{left:890px;top:0;width:250px;height:55px;background:var(--search);font-size:13px;font-style:italic;font-weight:400;color:#cfc8c2;padding:19px 0 0 22px}
.topbar .search svg{position:absolute;right:20px;top:18px}

/* nav */
.nav{left:0;top:55px;width:1200px;height:106px;background:var(--white)}
.brand{display:flex;align-items:center;gap:8px;font-weight:700;color:var(--green-dark);font-size:13px}
.brand .mark{width:16px;height:16px;background:var(--green)}
.nav .brand{left:92px;top:42px}
.menu{left:262px;top:42px;display:flex;gap:20px;font-size:14px;font-weight:500;color:#222}
.menu span{white-space:nowrap}
.btn-solid{background:var(--green-dark);color:var(--white);border-radius:24px;font-weight:700;text-align:center}
.nav .btn-solid{left:982px;top:33px;width:142px;height:41px;line-height:41px;font-size:14px}

/* hero */
.hero{left:0;top:161px;width:1200px;height:754px;background:linear-gradient(180deg,#7d8690 0%,#a9aeb2 45%,#6f6a60 100%)}
.pill{left:507px;top:291px;width:186px;height:40px;line-height:40px;border-radius:20px;background:var(--white);color:var(--green-dark);font-size:13px;font-weight:500;text-align:center}
.hero-title{left:0;width:1200px;text-align:center;font-family:"Poppins",sans-serif;color:var(--white)}
.hero-title.big{top:345px;font-size:80px;font-weight:700;line-height:96px}
.hero-title.sub{top:448px;font-size:50px;font-weight:400;line-height:62px}
.hero .btn-solid{left:510px;top:552px;width:180px;height:42px;line-height:42px;font-size:14px}

/* feature boxes */
.feature{top:728px;width:373px;height:371px;background:rgba(75,139,43,.82);color:var(--white);padding:48px 34px 0 34px}
.feature h3{font-size:20px;font-weight:700;line-height:25px;text-transform:uppercase;margin-bottom:12px}
.feature p{font-size:12px;line-height:17px}
.feature .btn-line{position:absolute;left:50%;transform:translateX(-50%);bottom:30px;width:128px;height:34px;line-height:32px;border:2px solid var(--white);border-radius:17px;font-size:12px;font-weight:500;text-align:center}
.arrow-tab{top:938px;width:34px;height:66px;background:var(--green)}

/* stats */
.stat{top:1168px;width:200px;text-align:center;color:var(--green-text)}
.stat svg{display:block;margin:0 auto}
.stat .num{font-size:26px;font-weight:700;color:var(--green-dark);margin-top:14px}
.stat .label{font-size:13px;font-weight:500;margin-top:6px}

/* mission cards */
.card{top:1425px;width:367px;height:671px;background:var(--grey-card)}
.card .photo{position:absolute;left:0;top:0;width:100%;height:318px}
.card .play{position:absolute;left:50%;top:159px;transform:translate(-50%,-50%)}
.card .band{position:absolute;left:0;top:318px;width:100%;height:46px;line-height:46px;background:var(--green-light);color:var(--white);text-align:center;font-size:22px;font-weight:700}
.card .body{position:absolute;left:14px;top:390px;width:336px}
.card h4{font-size:14px;font-weight:700;color:#222;margin-bottom:14px}
.card p{font-size:12px;line-height:17px;color:#333}
.card .more{font-size:11px;font-weight:500;margin-top:14px;color:#222}
.card .btn-line{position:absolute;left:50%;bottom:24px;transform:translateX(-50%);width:182px;height:40px;line-height:36px;border:2px solid var(--green-light);border-radius:20px;color:var(--green-dark);font-size:15px;font-weight:700;text-align:center}

/* donate section */
.donate-bg{left:0;top:2151px;width:1200px;height:728px;background:linear-gradient(135deg,#4a6a3a 0%,#6f8f5a 45%,#4e6744 100%)}
.donate-panel{left:88px;top:2202px;width:1022px;height:611px;background:rgba(120,160,100,.45)}
.donate-title{left:0;top:2262px;width:1200px;text-align:center;color:var(--white);font-size:36px;font-weight:700}
.field{height:51px;border:2px solid var(--white);color:var(--white);font-size:26px;padding:8px 8px;line-height:31px}
.field svg{position:absolute;right:12px;top:19px}
.donate-btn{left:488px;top:2678px;width:227px;height:51px;line-height:51px;font-size:24px;background:var(--green-light)}

/* footer logo + contact */
.footer-logo{left:539px;top:2824px;width:122px;height:99px;background:var(--white);display:flex;align-items:center;justify-content:center;flex-direction:column;gap:6px}
.contact-title{left:0;top:2950px;width:1200px;text-align:center;color:var(--green-light);font-size:36px;font-weight:700}
.office{top:3030px;color:var(--green-text);font-size:16px;line-height:22px}
.office h5{font-size:16px;font-weight:700;margin-bottom:18px;color:var(--green-dark)}
.mini-form .in{border:1.5px solid var(--green-light);height:18px;font-size:10px;color:var(--green-text);padding:1px 4px;margin-bottom:7px;width:177px}
.mini-form .in.tall{height:70px}
.mini-form .send{margin-left:0;width:55px;height:16px;line-height:16px;font-size:9px;background:var(--green-light);color:var(--white);border-radius:8px;text-align:center;font-weight:700;margin-top:8px}
.footer{left:0;top:3247px;width:1200px;height:62px;background:var(--green-dark);color:var(--white);text-align:center;line-height:62px;font-size:13px}
</style>
</head>
<body>

<header class="abs topbar">
  <span class="abs phone" style="left:88px">NEW YORK : 518-555-0147</span>
  <span class="abs phone" style="left:342px">TOLL FREE : (855) 555-0193</span>
  <div class="abs search">Type here to search
    <svg width="20" height="20" viewBox="0 0 20 20"><circle cx="8" cy="8" r="6" fill="none" stroke="#fff" stroke-width="2"/><line x1="12.5" y1="12.5" x2="18" y2="18" stroke="#fff" stroke-width="2"/></svg>
  </div>
</header>

<nav class="abs nav">
  <div class="abs brand"><span class="mark"></span>Brightwell Giving</div>
  <div class="abs menu">
    <span>HOME</span><span>MISSIONS ▾</span><span>HOW IT WORKS</span><span>ABOUT US ▾</span><span>SPONSORS</span><span>NEWS</span><span>WALL OF NEEDS</span>
  </div>
  <div class="abs btn-solid">DONATE NOW</div>
</nav>

<section class="abs hero" role="img" aria-label="Two volunteers standing beside a donation trailer outdoors"></section>
<div class="abs pill">HOW YOU COULD HELP</div>
<h1 class="abs hero-title big">Think Globally</h1>
<p class="abs hero-title sub">While Donating Locally</p>
<div class="abs btn-solid" style="left:510px;top:552px;width:180px;height:42px;line-height:42px;font-size:14px">LEARN MORE</div>

<div class="abs arrow-tab" style="left:0"><svg width="34" height="66" viewBox="0 0 34 66"><polyline points="21,22 12,33 21,44" fill="none" stroke="#fff" stroke-width="2"/></svg></div>
<div class="abs arrow-tab" style="left:1166px"><svg width="34" height="66" viewBox="0 0 34 66"><polyline points="13,22 22,33 13,44" fill="none" stroke="#fff" stroke-width="2"/></svg></div>

<article class="abs feature" style="left:40px">
  <h3>We are an open book organization</h3>
  <p>We collect gently used clothes and textiles from neighbors across the region, sort every donation with care, and pass it on to families who need it most, at home and around the world, keeping good fabric out of landfills.</p>
  <div class="btn-line">LEARN MORE</div>
</article>
<article class="abs feature" style="left:413px">
  <h3>We are a true 501(c)(3) non-profit organization</h3>
  <p>We collect gently used clothes and textiles from neighbors across the region, sort every donation with care, and pass it on to families who need it most, at home and around the world, keeping good fabric out of landfills.</p>
  <div class="btn-line">LEARN MORE</div>
</article>
<article class="abs feature" style="left:786px">
  <h3>Our goal is to be with and within the community</h3>
  <p>We collect gently used clothes and textiles from neighbors across the region, sort every donation with care, and pass it on to families who need it most, at home and around the world, keeping good fabric out of landfills.</p>
  <div class="btn-line">LEARN MORE</div>
</article>

<div class="abs stat" style="left:76px">
  <svg width="110" height="100" viewBox="0 0 110 100"><path d="M55 92 L14 52 A24 24 0 0 1 55 18 A24 24 0 0 1 96 52 Z" fill="none" stroke="#3a7020" stroke-width="7" stroke-linejoin="round"/><polyline points="4,54 36,54 44,40 54,68 62,46 68,54 106,54" fill="none" stroke="#3a7020" stroke-width="6" stroke-linejoin="round"/></svg>
  <div class="num">18934</div><div class="label">CAUSES</div>
</div>
<div class="abs stat" style="left:359px">
  <svg width="110" height="100" viewBox="0 0 110 100"><circle cx="30" cy="28" r="13" fill="none" stroke="#3a7020" stroke-width="6"/><circle cx="80" cy="28" r="13" fill="none" stroke="#3a7020" stroke-width="6"/><circle cx="55" cy="22" r="14" fill="none" stroke="#3a7020" stroke-width="6"/><path d="M12 80 V62 A18 18 0 0 1 30 46 M98 80 V62 A18 18 0 0 0 80 46 M30 86 V62 A25 25 0 0 1 80 62 V86" fill="none" stroke="#3a7020" stroke-width="6"/><circle cx="80" cy="78" r="17" fill="#3a7020"/><path d="M80 88 L72 80 A4.5 4.5 0 0 1 80 73 A4.5 4.5 0 0 1 88 80 Z" fill="#fff"/></svg>
  <div class="num">335845</div><div class="label">SAVED</div>
</div>
<div class="abs stat" style="left:643px">
  <svg width="110" height="100" viewBox="0 0 110 100"><circle cx="55" cy="50" r="44" fill="#3a7020"/><path d="M30 30 L48 26 L52 40 L40 50 L44 64 L34 72 L26 56 Z M62 20 L80 28 L86 46 L74 52 L66 40 Z M60 62 L76 60 L74 80 L62 84 Z" fill="#fff"/></svg>
  <div class="num">1434</div><div class="label">PLACES</div>
</div>
<div class="abs stat" style="left:919px">
  <svg width="110" height="100" viewBox="0 0 110 100"><path d="M40 98 V58 L28 42 V20 L34 20 V40 L38 40 V10 L44 10 V38 L48 38 V6 L54 6 V38 L58 38 V12 L64 12 V56 L70 46 L76 50 L62 76 V98 Z" fill="#3a7020"/><path d="M10 98 V70 L2 56 L6 54 L14 64 V40 L19 40 V62 L22 62 V36 L27 36 V70 L22 98 Z" fill="#3a7020"/><path d="M80 98 V72 L74 60 L78 58 L84 66 V42 L89 42 V62 L92 62 V38 L97 38 V62 L100 62 V44 L105 44 V74 L98 98 Z" fill="#3a7020"/></svg>
  <div class="num">5934</div><div class="label">VOLUNTEERS</div>
</div>

<article class="abs card" style="left:40px">
  <div class="photo" role="img" aria-label="Classroom with wooden benches in Haiti" style="background:linear-gradient(160deg,#a89a88,#5e4f42)"></div>
  <svg class="play" width="92" height="92" viewBox="0 0 92 92"><circle cx="46" cy="46" r="40" fill="none" stroke="#4b8b2b" stroke-width="7"/><polygon points="36,28 64,46 36,64" fill="#4b8b2b"/></svg>
  <div class="band">HAITI</div>
  <div class="body">
    <h4>HAITI STATEMENTS</h4>
    <p>Harvest Learning Centre (H.L.C) is a non governmental organisation where young adult students learn how to grow vegetables and plants that protect the environment. Together with Brightwell Giving, we will bring a new modern farming method to Haiti and open an exchange.</p>
    <div class="more">READ MORE&gt;&gt;</div>
  </div>
  <div class="btn-line">DONATE NOW</div>
</article>
<article class="abs card" style="left:419px">
  <div class="photo" role="img" aria-label="Volunteers with a large family receiving aid in Ukraine" style="background:linear-gradient(160deg,#b7b2aa,#6a5f58)"></div>
  <div class="band">UKRAINE</div>
  <div class="body">
    <h4>UKRAINE STATEMENTS</h4>
    <p>We brought humanitarian aid to large families this winter. Warm coats, boots and blankets reached homes in need, and volunteers stayed to share a meal. When you come to the needy, do not come with empty hands; bring hope and a helping hand.</p>
    <div class="more">READ MORE&gt;&gt;</div>
  </div>
  <div class="btn-line">DONATE NOW</div>
</article>
<article class="abs card" style="left:794px">
  <div class="photo" role="img" aria-label="Mother holding her young daughter at home" style="background:linear-gradient(160deg,#c9bfb8,#7a6c66)"></div>
  <svg class="play" width="92" height="92" viewBox="0 0 92 92"><circle cx="46" cy="46" r="40" fill="none" stroke="#4b8b2b" stroke-width="7"/><polygon points="36,28 64,46 36,64" fill="#4b8b2b"/></svg>
  <div class="band">LOVE THY NEIGHBOR-ELENA</div>
  <div class="body">
    <h4>HAITI STATEMENTS</h4>
    <p>We would like to thank everyone who took part in the charitable project for Elena. Our shared efforts gathered enough to fund her rehabilitation clinic stay. We thank all who donated, bought clothes and joined the project through their gifts.</p>
    <div class="more">READ MORE&gt;&gt;</div>
  </div>
  <div class="btn-line">DONATE NOW</div>
</article>

<section class="abs donate-bg" role="img" aria-label="Volunteer standing beside a green clothing donation trailer"></section>
<div class="abs donate-panel"></div>
<h2 class="abs donate-title">MAKE A DONATION NOW!</h2>
<div class="abs field" style="left:205px;top:2347px;width:364px">Name</div>
<div class="abs field" style="left:631px;top:2347px;width:364px">Email</div>
<div class="abs field" style="left:205px;top:2453px;width:364px">Donation place<svg width="14" height="10" viewBox="0 0 14 10"><polyline points="1,1 7,8 13,1" fill="none" stroke="#fff" stroke-width="1.5"/></svg></div>
<div class="abs field" style="left:631px;top:2453px;width:364px">Donation amount</div>
<div class="abs field" style="left:205px;top:2561px;width:790px;height:56px">I Want to Donate For<svg width="14" height="10" viewBox="0 0 14 10"><polyline points="1,1 7,8 13,1" fill="none" stroke="#fff" stroke-width="1.5"/></svg></div>
<div class="abs btn-solid donate-btn">DONATE</div>

<div class="abs footer-logo"><span class="brand"><span class="mark"></span></span><span class="brand" style="font-size:12px">Brightwell Giving</span></div>

<h2 class="abs contact-title">CONTACT US</h2>
<div class="abs office" style="left:99px"><h5>NEW YORK OFFICE</h5>42 Orchard Ct<br>Millbrook NY 12545<br>(855) 555-0193</div>
<div class="abs office" style="left:393px"><h5>NY WAREHOUSE</h5>1180 Route 52<br>Kerhonkson<br>NY 12446</div>
<div class="abs office" style="left:675px"><h5>THRIFT STORE</h5>96 Linden St<br>Rhinecliff<br>NY 12574</div>
<div class="abs mini-form" style="left:935px;top:3031px">
  <div class="in">Name</div>
  <div class="in">Email</div>
  <div class="in tall">Message</div>
  <div class="send">SEND</div>
</div>

<footer class="abs footer">Copyright © 2018 All rights reserved. <b>Brightwell Giving</b></footer>

</body>
</html>
```